IT Company requires new Business Card design.

Over the years we have had a few different business card designs. We are now due for new cards across the board for all staff. We felt this would be a good time to start fresh with a new design. Our traditional card simply had our details on the front, and a list of services on the back. We don't particularly need the list of services, we have had cards where the only thing on the rear of the card was our logo.
Feel free to be creative, we would like our tag line "Complete IT Management" to appear at some point, doesn't necessarily have to be with the logo.
I have attached samples and drafts of various previous cards we have used over the years.

```html
<!DOCTYPE html>
<html lang="en">
<head>
<meta charset="utf-8">
<title>Ridgeway Systems – Business Card</title>
<link rel="stylesheet" href="https://fonts.googleapis.com/css2?family=Archivo:wght@700&family=Questrial&display=swap">
<style>
  :root {
    --brand: #4e7a8f;
    --ink: #111111;
    --paper: #ffffff;
  }
  * { box-sizing: border-box; margin: 0; padding: 0; }
  html, body {
    width: 1200px;
    height: 750px;
    overflow: hidden;
    background: var(--paper);
  }
  .card {
    position: relative;
    width: 1200px;
    height: 750px;
    background: var(--paper);
    font-family: "Questrial", "Century Gothic", sans-serif;
    color: var(--ink);
  }

  /* Brand lockup */
  .brand-square {
    position: absolute;
    left: 300px;
    top: 96px;
    width: 170px;
    height: 170px;
    background: var(--brand);
  }
  .brand-name {
    position: absolute;
    left: 526px;
    top: 74px;
    font-family: "Archivo", "Arial", sans-serif;
    font-weight: 700;
    color: var(--brand);
    line-height: 1;
  }
  .brand-name .line-one {
    display: block;
    font-size: 84px;
    letter-spacing: -1px;
  }
  .brand-name .line-two {
    display: block;
    font-size: 50px;
    margin-top: 10px;
    letter-spacing: 0.5px;
  }
  .tagline {
    position: absolute;
    left: 528px;
    top: 226px;
    font-family: "Questrial", "Century Gothic", sans-serif;
    font-size: 22px;
    letter-spacing: 4.1px;
    color: var(--brand);
    white-space: nowrap;
  }

  /* Person block */
  .person-icon {
    position: absolute;
    left: 71px;
    top: 426px;
    width: 56px;
    height: 56px;
  }
  .person-name {
    position: absolute;
    left: 140px;
    top: 414px;
    font-size: 43px;
    line-height: 1;
    letter-spacing: 0.5px;
  }
  .person-role {
    position: absolute;
    left: 141px;
    top: 461px;
    font-size: 33px;
    line-height: 1;
  }

  .divider {
    position: absolute;
    left: 487px;
    top: 353px;
    width: 2px;
    height: 225px;
    background: var(--brand);
  }

  /* Contact list */
  .contact-list {
    position: absolute;
    left: 524px;
    top: 379px;
    list-style: none;
  }
  .contact-item {
    display: flex;
    align-items: flex-start;
    font-size: 27px;
    line-height: 34px;
    margin-bottom: 8px;
  }
  .contact-item svg {
    flex: 0 0 30px;
    width: 30px;
    height: 30px;
    margin-top: 2px;
    margin-right: 15px;
  }

  .web-address {
    position: absolute;
    left: 0;
    width: 1220px;
    top: 694px;
    text-align: center;
    font-family: "Archivo", "Arial", sans-serif;
    font-weight: 700;
    font-size: 34px;
    color: var(--brand);
    letter-spacing: 0.3px;
  }
</style>
</head>
<body>
<div class="card">

  <div class="brand-square" aria-hidden="true"></div>
  <div class="brand-name">
    <span class="line-one">RIDGEWAY</span>
    <span class="line-two">SYSTEMS</span>
  </div>
  <div class="tagline">COMPLETE IT MANAGEMENT</div>

  <svg class="person-icon" viewBox="0 0 56 56" aria-hidden="true">
    <circle cx="28" cy="28" r="28" fill="var(--brand)"/>
    <circle cx="28" cy="22" r="8.5" fill="#fff"/>
    <path d="M13 41 C13 32 20 30 28 30 C36 30 43 32 43 41 Z" fill="#fff"/>
  </svg>
  <div class="person-name">YOUR NAME</div>
  <div class="person-role">Company Position</div>

  <div class="divider"></div>

  <ul class="contact-list">
    <li class="contact-item">
      <svg viewBox="0 0 30 30" aria-hidden="true">
        <circle cx="15" cy="15" r="13.5" fill="none" stroke="var(--ink)" stroke-width="1.8"/>
        <path d="M10 8.5 l3 -0.5 l1.5 4 l-2 1.3 q1.3 3 4 4.5 l1.4 -2 l4 1.5 l-0.5 3 q-7 1 -11.4 -11.8 z" fill="none" stroke="var(--ink)" stroke-width="1.5" stroke-linejoin="round"/>
      </svg>
      <span>08 5550 1840</span>
    </li>
    <li class="contact-item">
      <svg viewBox="0 0 30 30" aria-hidden="true">
        <circle cx="15" cy="15" r="13.5" fill="none" stroke="var(--ink)" stroke-width="1.8"/>
        <rect x="10.5" y="7.5" width="9" height="4.5" fill="var(--ink)"/>
        <rect x="7.5" y="12.5" width="15" height="7" rx="1" fill="var(--ink)"/>
        <rect x="10.5" y="17" width="9" height="6" fill="#fff" stroke="var(--ink)" stroke-width="1.3"/>
      </svg>
      <span>08 5550 1842</span>
    </li>
    <li class="contact-item">
      <svg viewBox="0 0 30 30" aria-hidden="true">
        <circle cx="15" cy="15" r="13.5" fill="none" stroke="var(--ink)" stroke-width="1.8"/>
        <rect x="8" y="10" width="14" height="10" fill="var(--ink)"/>
        <path d="M8 10 L15 16 L22 10" fill="none" stroke="#fff" stroke-width="1.3"/>
      </svg>
      <span>support@ridgewaysystems.com.au</span>
    </li>
    <li class="contact-item">
      <svg viewBox="0 0 30 30" aria-hidden="true">
        <circle cx="15" cy="15" r="13.5" fill="none" stroke="var(--ink)" stroke-width="1.8"/>
        <path d="M7 15 L15 8 L23 15 L21 15 L21 22 L17 22 L17 17.5 L13 17.5 L13 22 L9 22 L9 15 Z" fill="var(--brand)"/>
      </svg>
      <span>Unit 4, 18 Marlow Street, Kinsale Park<br>WA 6190</span>
    </li>
  </ul>

  <div class="web-address">web@ridgewaysystems.com.au</div>

</div>
</body>
</html>
```